Flyer-Design für Flugzeugvercharterung
Zielgruppe
Lenz-Tal Aviation ist ein junges Unternehmen in dem Bereich Flugzeugvercharterung für Falkor Aircraft Flugzeuge.
Wir haben es uns zum Ziel gemacht, unseren Kunden Flugstunden zu einem fairen Preis anzubieten.
Sicherheit beim Fliegen steht für uns im Fokus – jederzeit sorgen wir für einen einwandfreien Zustand der Technik. Die Wartung und Instandhaltung unserer Flotte wird dabei durch die Herstellerwerft Falkor Aircraft gewährleistet. Fliegen Sie mit uns und lernen Sie die Vorteile unseres Charter-Unternehmens kennen!
Aufgabenstellung
Der Flyer muss ansprechend sein.
Der Flyer muss modern sein - aber nicht verspielt.
Der Kunde muss den Flyer in die Hand nehmen und einen "Wow" Effekt erhalten.
Nutzen Sie alle informationen auf unserer Webpage: www.LT-Aviation-beispiel.de
Es sollen mindestens dreifach sein - evtl sogar vierfach! (Also drei pro Seite, wenn der flyer gewendet wird)
Wir bieten eines der modernsten Flugzeuge im General Aviation Bereich an. Dies soll der Kunde sofort erkennen. Gleichzeitig sind wir sehr professionell - aber keine Spießer-Firma.
Profi ja - Spießer nein.
Mein Kooperationspartern hat in meinen Augen einen sehr guten Flyer erstellt (siehe Anhang).
Ebenfalls habe ich "meinen" Versuch eines Flyers mal angehängt.
Was benötigen wir?
- Einen modernen aber stylischen Auftritt
- Alles auf einen Blick
- Gute Ausführungen unserer Flugzeuge (hierzu kann gerne die HP genutzt werden "www.LT-Aviation-beispiel.de"
- Anlehnung an die Homepage www.LT-Aviation-beispiel.de
So kann evtl ein direkter Bezug hergestellt werden.

```html
<!DOCTYPE html>
<html lang="de">
<head>
<meta charset="utf-8">
<title>Lenz-Tal Aviation – Flyer</title>
<link rel="stylesheet" href="https://fonts.googleapis.com/css2?family=Ubuntu:wght@300;400;500;700&display=swap">
<style>
  :root {
    --page: #ffffff;
    --ink: #18141f;
    --text: #f1f1f4;
    --cyan: #4fb3e6;
    --stripe-sky: #5bb4e0;
    --stripe-mid: #3f6fae;
    --stripe-deep: #3a4694;
    --panel-blue: #4a78b8;
    --tile-blue: #4e7fbf;
    --tile-light: #6fa3d6;
    --logo-box: #e8e8ec;
    --logo-ink: #2f3f8f;
  }
  * { margin: 0; padding: 0; box-sizing: border-box; }
  html, body { width: 713px; height: 1200px; overflow: hidden; background: var(--page); }
  body { font-family: "Ubuntu", sans-serif; color: var(--text); position: relative; }

  .spread { position: absolute; left: 20px; width: 673px; height: 475px; overflow: hidden; background: var(--ink); }
  .spread--outside { top: 115px; }
  .spread--inside { top: 610px; }

  .panel { position: absolute; top: 0; height: 100%; }
  .stripes { position: absolute; display: flex; height: 11px; }
  .stripes span { flex: 1; }
  .stripes span:nth-child(1) { background: var(--stripe-sky); }
  .stripes span:nth-child(2) { background: var(--stripe-mid); }
  .stripes span:nth-child(3) { background: var(--stripe-deep); }

  .photo { position: absolute; }

  .copy { font-size: 6.9px; line-height: 1.62; font-weight: 300; }
  .copy p + p { margin-top: 9px; }
  .copy--justify { text-align: justify; }

  /* Outside spread */
  .intro { left: 0; width: 220px; }
  .intro-title { position: absolute; top: 36px; left: 18px; right: 18px; text-align: center; color: var(--cyan); font-weight: 300; font-size: 17px; line-height: 1.5; }
  .intro .copy { position: absolute; top: 122px; left: 20px; right: 20px; }
  .intro .stripes { top: 292px; left: 0; width: 220px; }
  .intro .photo { top: 303px; left: 0; width: 220px; height: 172px; background: linear-gradient(100deg, #e9e8ec 0%, #c9cbd6 45%, #e2c7a8 75%, #f1d9b8 100%); }

  .find { left: 220px; width: 226px; }
  .find-title { position: absolute; top: 36px; left: 20px; color: var(--cyan); font-weight: 300; font-size: 17px; }
  .find .copy { position: absolute; top: 70px; left: 20px; right: 20px; }
  .find .stripes { top: 308px; left: 0; width: 226px; }
  .contact { position: absolute; top: 346px; left: 0; right: 0; text-align: center; font-size: 6.9px; line-height: 1.75; font-weight: 300; }
  .contact-name { color: var(--cyan); font-weight: 700; font-size: 9.5px; margin-bottom: 10px; }

  .cover { left: 446px; width: 227px; }
  .cover .stripes { top: 0; left: 0; width: 227px; height: 8px; }
  .cover .photo--sky { top: 8px; left: 0; width: 227px; height: 163px; background: linear-gradient(180deg, #2a3363 0%, #4a4f86 40%, #8a6e96 70%, #3f5ea3 100%); }
  .tiles { position: absolute; top: 171px; left: 0; width: 227px; height: 304px; display: grid; grid-template-columns: repeat(3, 1fr); grid-template-rows: repeat(4, 1fr); }
  .tile--city { background: linear-gradient(160deg, #7a5a3c, #c98a4a 55%, #3a3040); }
  .tile--dusk { background: linear-gradient(160deg, #a5825f, #e0a66a 55%, #5a4b61); }
  .tile--blue { background: var(--tile-blue); }
  .tile--light { background: var(--tile-light); }
  .tile--night { background: linear-gradient(160deg, #2d2a3a, #8c4d2a 60%, #d08a3a); }
  .tile--logo { grid-column: 2 / 4; background: var(--logo-box); display: flex; align-items: center; justify-content: center; gap: 6px; }
  .logo-mark { width: 9px; height: 9px; background: var(--logo-ink); }
  .logo-name { color: var(--logo-ink); font-weight: 700; font-size: 13px; }

  /* Inside spread */
  .hero { position: absolute; top: 0; left: 0; width: 673px; height: 156px; background: linear-gradient(180deg, #6f7358 0%, #8e9a5a 40%, #b7c07a 55%, #dfe0dd 56%, #eeeef0 80%, #b9c6e0 100%); }
  .hero-name { position: absolute; top: 40px; right: 26px; display: flex; align-items: center; gap: 6px; }
  .hero .logo-name { font-size: 16px; }
  .spread--inside > .stripes { top: 156px; left: 0; width: 673px; height: 8px; }

  .column { top: 164px; height: 311px; }
  .column h2 { position: absolute; top: 6px; left: 9px; font-size: 13.5px; font-weight: 500; }
  .column .copy { position: absolute; top: 34px; left: 9px; right: 9px; }

  .charter { left: 0; width: 225px; background: var(--ink); }
  .charter h2 { color: var(--cyan); }
  .fleet { margin-top: 9px; color: var(--cyan); }
  .fleet li { list-style: none; }
  .fleet li + li { margin-top: 7px; }
  .charter .stripes { bottom: 0; left: 0; width: 225px; height: 8px; }

  .flights { left: 225px; width: 224px; background: var(--panel-blue); }
  .flights h2 { color: #ffffff; }
  .flights strong { font-weight: 700; }

  .training { left: 449px; width: 224px; background: var(--ink); }
  .training h2 { color: var(--cyan); }
  .training .photo { top: 220px; left: 0; width: 224px; height: 91px; background: linear-gradient(180deg, #7d93b8 0%, #5d6470 30%, #3a3c44 70%, #55585f 100%); }
  .training .stripes { top: 220px; left: 0; width: 224px; height: 0; }
</style>
</head>
<body>

<section class="spread spread--outside">
  <div class="panel intro">
    <h1 class="intro-title">Noch nie war<br>Fliegen so sicher &amp;<br>günstig zugleich</h1>
    <div class="copy">
      <p>Lenz-Tal Aviation ist ein Charter-Unternehmen, das es sich zur Aufgabe gemacht hat, Hobby- bzw. Berufspiloten faire, preiswerte Flugstunden zu ermöglichen! Auch Flugbegeisterte können bei unseren Schnupperflügen die Welt von oben betrachten und auf Wunsch ihre Pilotenausbildung bei uns beginnen.</p>
      <p>Sehr gerne informieren wir Sie zu unserem Leistungsangebot – rufen Sie an oder kommen Sie bei uns in Lenztal vorbei.</p>
    </div>
    <div class="stripes"><span></span><span></span><span></span></div>
    <div class="photo" role="img" aria-label="Foto: Nahaufnahme eines weißen Kleinflugzeugs vor einer Stadtsilhouette"></div>
  </div>

  <div class="panel find">
    <h2 class="find-title">So finden Sie uns</h2>
    <div class="copy copy--justify">
      <p>Wir sind in Lenztal im Haus von Falkor Aircraft untergebracht. Mit dem Auto können Sie auf das Gelände von Falkor Aircraft fahren und es auf den Parkplätzen neben dem Gebäude parken. Auf dieser Seite befindet sich ebenfalls der Eingang. Wir sind täglich ab 09:30 Uhr für Sie da.</p>
      <p>Im Foyer liegen unsere Flyer und Informationsbroschüren aus – hier finden Sie alle notwendigen Informationen vor.</p>
      <p>Besuchen Sie uns mit den öffentlichen Verkehrsmitteln: Fahren Sie mit der S-Bahn S3 bis zum Bahnhof Lenztal und folgen anschließend dem Fußweg in Richtung des Flugplatzes Lenztal in südlicher Richtung.</p>
    </div>
    <div class="stripes"><span></span><span></span><span></span></div>
    <address class="contact">
      <div class="contact-name">Lenz-Tal Aviation</div>
      Im Haus von Falkor Aircraft<br>
      Am Flugfeld 14<br>
      63399 Lenztal<br>
      Tel.: 06100 - 555 012 34<br>
      e-mail: info@lt-aviation-beispiel.de<br>
      www.LT-Aviation-beispiel.de
    </address>
  </div>

  <div class="panel cover">
    <div class="stripes"><span></span><span></span><span></span></div>
    <div class="photo photo--sky" role="img" aria-label="Foto: Verkehrsflugzeug im Anflug vor Abendhimmel"></div>
    <div class="tiles">
      <div class="tile--blue"></div>
      <div class="tile--dusk" role="img" aria-label="Foto: Stadt im Abendlicht"></div>
      <div class="tile--light"></div>
      <div class="tile--city" role="img" aria-label="Foto: Stadt von oben"></div>
      <div class="tile--blue"></div>
      <div class="tile--light"></div>
      <div class="tile--light"></div>
      <div class="tile--logo"><span class="logo-mark"></span><span class="logo-name">Lenz-Tal Aviation</span></div>
      <div class="tile--night" role="img" aria-label="Foto: Stadt bei Nacht"></div>
      <div class="tile--blue"></div>
      <div class="tile--light"></div>
    </div>
  </div>
</section>

<section class="spread spread--inside">
  <div class="hero" role="img" aria-label="Foto: weißes Kleinflugzeug mit Firmenschriftzug auf dem Flugfeld">
    <div class="hero-name"><span class="logo-mark"></span><span class="logo-name">Lenz-Tal Aviation</span></div>
  </div>
  <div class="stripes"><span></span><span></span><span></span></div>

  <div class="panel column charter">
    <h2>Charter &amp; Flotte</h2>
    <div class="copy copy--justify">
      <p>Unsere Preise verstehen sich inklusive 19 % Mehrwertsteuer und Treibstoffkosten. Landegebühren, Abstellgebühren sowie Handling-Fees der jeweiligen Airports usw. sind nicht im Preis enthalten.</p>
      <p>Abgerechnet wird nach Blockstunden in den jeweiligen Flugzeugen. Die Stundenzähler werden vor und nach jedem Flug von einem unserer Mitarbeiter gemeinsam mit Ihnen abgelesen und in das Übergabeprotokoll eingetragen. So haben Sie eine transparente Übersicht. Zu jeder Abrechnung erhalten Sie vor Ort eine Rechnung.</p>
      <ul class="fleet">
        <li>• FK20-100 mit Navi 660<br>159€ pro Stunde Nassmiete</li>
        <li>• FK40 IFR/AP OE-XQA<br>249€ pro Stunde Nassmiete</li>
        <li>• FK42 TDI OE-XYZ<br>319€ pro Stunde Nassmiete</li>
      </ul>
    </div>
    <div class="stripes"><span></span><span></span><span></span></div>
  </div>

  <div class="panel column flights">
    <h2>Rundflüge</h2>
    <div class="copy">
      <p>Die Welt von oben sehen – Wir machen es möglich</p>
      <p>Die Frankfurter Skyline aus der Vogelperspektive betrachten? Das eigene Haus, Ihre Wohnung oder den Garten von oben sehen? Dann sind Sie bei der Lenz-Tal Aviation in Lenztal genau richtig.</p>
      <p>So könnte Ihr Rundflug aussehen:</p>
      <p><strong>Beispiel 1:</strong> Platzrunden-Rundflug mit 1 Person (max. 100 Kg) ab Lenztal für 29€</p>
      <p><strong>Beispiel 2:</strong> 30 Minuten Rundflug für 1 Person (max. 100 Kg) ab Lenztal für 109€ (ideal für einen Skyline Rundflug), aktuell für 99€.</p>
      <p><strong>Beispiel 3:</strong> 30 Minuten Rundflug mit bis zu 3 Personen (insg. max. 200 Kg) ab Lenztal für 199€ regulär (ideal für einen Skyline Rundflug), aktuell für 179€.</p>
    </div>
  </div>

  <div class="panel column training">
    <h2>Pilotenausbildung</h2>
    <div class="copy copy--justify">
      <p>In Zusammenarbeit mit unserem Kooperationspartnern können Sie bei der Lenz-Tal Aviation ab sofort Pilot werden! Sie haben die Möglichkeit im Rahmen unserer Pilotenausbildung die Flugscheine PPL-A bis ATPL-A zu erreichen.</p>
      <p>Ihre praktische Flugausbildung werden Sie auf der modernen Flotte von Lenz-Tal Aviation durchführen. Der Vorteil dabei: Sie werden von den klassischen Fluginstrumenten bis hin zum modernen „Glascockpit“ ein abgerundetes Angebot erhalten – und jederzeit selbst entscheiden dürfen, ob Sie klassische Instrumente oder moderne Anzeigegeräte bevorzugen.</p>
    </div>
    <div class="photo" role="img" aria-label="Foto: Cockpit mit Rundinstrumenten"></div>
  </div>
</section>

</body>
</html>
```